stars + comments Reviews website design (similar to quarn concept)

Please refer to attached logo and wire frames
----------------------------------------------------------------------------------------------------
we are a company based in egypt, seeking a design for a website that allows user to find doctors using search and filters.
also it allows user to review this doctor through providing comment and 1 to 5 stars
i need 4 main pages designs:
1- Doctors list/favorites list
2- Doctor view
3- Add doctor (3 steps)
4- Sign-in/sign up
5- Menu design
am into the colors teal/turquoise (though am open for different opinion)
i don't want the design theme to be doctors specific
am into the school of very clean, very neat, very simple
(plombex, ruvanteo, melvoshade designs are appealing to me)

Number of Pages Required

4 page

Font styles to use
Sans Serif

Colors
00a990
33b8a4

Requirements
Must have
• website will be bilingual/ bi-directional (English and Arabic)
• designer needs to provide another copy of the design with "right to left" orientation
• interactive button animation

```html
<!DOCTYPE html>
<html lang="en">
<head>
<meta charset="utf-8">
<title>Ratewise – Add Doctor</title>
<link rel="stylesheet" href="https://fonts.googleapis.com/css2?family=Arimo:wght@400;700&family=Nunito:wght@700;800&display=swap">
<style>
  :root {
    --teal: #009a94;
    --page-bg: #e8e6df;
    --panel-bg: #f8f7f4;
    --ink: #222222;
    --muted: #555555;
    --field-border: #7cc6c0;
    --icon-dark: #222222;
    --accent-red: #e8303f;
    --step-1: #232323;
    --step-2: #4b4b4b;
    --step-3: #757575;
    --white: #ffffff;
  }
  * { box-sizing: border-box; margin: 0; padding: 0; }
  html, body { width: 1200px; height: 731px; overflow: hidden; }
  body {
    position: relative;
    background: var(--page-bg);
    font-family: "Arimo", Arial, sans-serif;
    color: var(--ink);
  }
  .site-header {
    position: absolute; left: 0; top: 0; width: 1200px; height: 103px;
    background: var(--teal);
    border-bottom: 5px solid var(--white);
    height: 108px;
  }
  .brand {
    position: absolute; left: 105px; top: 22px;
    font-family: "Nunito", sans-serif; font-weight: 800;
    font-size: 50px; line-height: 60px; color: var(--white);
    letter-spacing: -0.5px;
  }
  .nav-icon {
    position: absolute; top: 32px; width: 50px; height: 50px;
    border-radius: 50%; background: var(--icon-dark);
  }
  .nav-icon svg { display: block; }
  .nav-icon.is-active { background: var(--accent-red); }
  .user-menu {
    position: absolute; left: 949px; top: 37px; width: 121px; height: 35px;
    border: 1px solid rgba(255,255,255,0.8);
    color: var(--white); font-size: 15px; line-height: 33px; padding-left: 12px;
  }
  .user-menu .caret {
    position: absolute; right: 12px; top: 15px;
    border-left: 5px solid transparent; border-right: 5px solid transparent;
    border-top: 5px solid var(--white);
  }
  .form-panel {
    position: absolute; left: 138px; top: 156px; width: 915px; height: 508px;
    background: var(--panel-bg);
    box-shadow: 0 1px 4px rgba(0,0,0,0.12);
  }
  .steps { position: absolute; left: 91px; top: 30px; }
  .step-label {
    font-family: "Nunito", sans-serif; font-weight: 800; font-size: 26px; fill: var(--white);
  }
  .photo-slot { position: absolute; left: 94px; top: 173px; width: 99px; }
  .photo-fill {
    height: 98px;
    background: linear-gradient(180deg, #8f8473 0%, #b9b1a3 55%, #e8e8e6 100%);
  }
  .photo-caption {
    height: 68px; background: var(--white); border: 1px solid #999;
    text-align: center; font-size: 13px; line-height: 20px; padding-top: 11px;
  }
  .photo-caption b { display: block; font-weight: 700; }
  .field {
    position: absolute; height: 38px; border: 1px solid var(--field-border);
    border-radius: 10px; background: var(--white);
    font-size: 13px; color: var(--muted); line-height: 36px; padding-left: 11px;
  }
  .field.select .caret {
    position: absolute; right: 13px; top: 16px;
    border-left: 5px solid transparent; border-right: 5px solid transparent;
    border-top: 5px solid #333;
  }
  .gender { position: absolute; top: 241px; font-size: 15px; line-height: 20px; }
  .radio {
    display: inline-block; width: 18px; height: 18px; border-radius: 50%;
    border: 1px solid #888; background: var(--white); vertical-align: -4px; margin-right: 6px;
    position: relative;
  }
  .radio.is-checked::after {
    content: ""; position: absolute; left: 4px; top: 4px; width: 8px; height: 8px;
    border-radius: 50%; background: #86c440;
  }
  .btn {
    position: absolute; top: 371px; width: 106px; height: 36px; border-radius: 4px;
    color: var(--white); font-weight: 700; font-size: 14px; text-align: center; line-height: 32px;
    border: 2px solid var(--white);
  }
  .btn-cancel { left: 575px; background: linear-gradient(#4a4a4a, #1e1e1e); box-shadow: 0 0 0 1px #222; }
  .btn-next { left: 717px; background: linear-gradient(#f0485a, #d8223a); box-shadow: 0 0 0 1px #d8223a; }
  .site-footer {
    position: absolute; left: 0; top: 691px; width: 1266px; text-align: center;
    font-size: 13px; color: var(--ink);
  }
</style>
</head>
<body>
  <header class="site-header">
    <div class="brand">Ratewise</div>
    <a class="nav-icon" style="left:522px" aria-label="Home">
      <svg width="50" height="50" viewBox="0 0 50 50"><path d="M25 11 L41 25 L37 25 L37 38 L29 38 L29 30 L21 30 L21 38 L13 38 L13 25 L9 25 Z" fill="#fff"/></svg>
    </a>
    <a class="nav-icon is-active" style="left:646px" aria-label="Favorites">
      <svg width="50" height="50" viewBox="0 0 50 50"><path d="M25 38 C12 29 11 22 13 18 C16 13 22 13 25 18 C28 13 34 13 37 18 C39 22 38 29 25 38 Z" fill="#fff"/></svg>
    </a>
    <a class="nav-icon" style="left:772px" aria-label="Add doctor">
      <svg width="50" height="50" viewBox="0 0 50 50"><circle cx="23" cy="18" r="6" fill="#fff"/><path d="M12 36 C12 28 17 25 23 25 C28 25 30 27 31 28 L31 36 Z" fill="#fff"/><circle cx="32" cy="32" r="6" fill="#fff"/><path d="M32 29 V35 M29 32 H35" stroke="#222" stroke-width="2"/></svg>
    </a>
    <div class="user-menu">Admin Sam<span class="caret"></span></div>
  </header>

  <main class="form-panel">
    <svg class="steps" width="735" height="74" viewBox="0 0 735 74">
      <polygon points="0,0 208,0 245,36 208,72 0,72 37,36" fill="var(--step-1)"/>
      <polyline points="14,5 206,5 238,36 206,67 14,67 45,36 14,5" fill="none" stroke="#777" stroke-width="1"/>
      <text class="step-label" x="129" y="45" text-anchor="middle">Basic Info</text>
      <polygon points="242,0 453,0 490,36 453,72 242,72 279,36" fill="var(--step-2)"/>
      <polyline points="256,5 451,5 483,36 451,67 256,67 287,36 256,5" fill="none" stroke="#999" stroke-width="1"/>
      <text class="step-label" x="366" y="45" text-anchor="middle">Address</text>
      <polygon points="484,0 696,0 733,36 696,72 484,72 521,36" fill="var(--step-3)"/>
      <polyline points="498,5 694,5 726,36 694,67 498,67 529,36 498,5" fill="none" stroke="#aaa" stroke-width="1"/>
      <text class="step-label" x="608" y="45" text-anchor="middle">Review</text>
    </svg>

    <div class="photo-slot">
      <div class="photo-fill" role="img" aria-label="Doctor portrait photo"></div>
      <div class="photo-caption"><b>Add Photo</b>(Optional)</div>
    </div>

    <div class="field" style="left:235px; top:172px; width:325px; border-radius:12px;">Doctor Name</div>

    <div class="gender" style="left:406px;"><span class="radio is-checked"></span>Male</div>
    <div class="gender" style="left:485px;"><span class="radio"></span>Female</div>

    <div class="field select" style="left:606px; top:173px; width:218px;">Egypt<span class="caret"></span></div>
    <div class="field select" style="left:606px; top:236px; width:218px;">Specialization<span class="caret"></span></div>
    <div class="field select" style="left:606px; top:302px; width:218px;">Sub Specialization<span class="caret"></span></div>

    <div class="btn btn-cancel">Cancel</div>
    <div class="btn btn-next">Next</div>
  </main>

  <footer class="site-footer">Copyright © 2015 The Ratewise. Powered by Pressly and Arvent</footer>
</body>
</html>
```